Partnership Enterprise Architects looking for Business Flyer (Dutch laguage)

We are a partnership of independent IT Architects working in various roles within our clients (Goverment agencies, Financial institutions and for profit companies). With this flyer we would like to promote ourselves in a inviting but still business like way. We would like to see our logo and name (Maatschap Veltrix) and the graphs and text we used in our example as the basis of the flyer. Anything else is up to your creativity. Colors and 'look and feel' of the graphs may be altered as long as the text (Dutch language remains unchanged). We think a 2 page A4 format flyer would serve best, but are open to suggestions.

Target Market(s)

Clients in the field of Government agencies, Financial institutions and for profit comapnies as well as possible future partners in the ICT Architect field

Industry/Entity Type

Business

Font styles to use
Sans Serif
Other font styles liked:
• Calibri 11 is our standard font

Colors

Designer to choose colors to be used in the design.

Requirements
Must have
• The text (verbatim in the Dutch laguage) as well as the graphs (they may be altered as you see fit as long as the general point and meaning remain the same). Logo preferably upper right corner. 2 A4 double sided flyer in one piece (

```html
<!DOCTYPE html>
<html lang="nl">
<head>
<meta charset="utf-8">
<title>Maatschap Veltrix – flyer</title>
<link href="https://fonts.googleapis.com/css2?family=Oswald:wght@500&family=Carlito:wght@400&display=swap" rel="stylesheet">
<style>
  :root {
    --teal: #95cfc0;
    --cream: #f4f0e6;
    --slate: #4a4e5f;
    --slate-dark: #3f4352;
    --purple: #9a58a6;
    --lilac: #b08fd6;
    --paper: #ffffff;
    --text: #262626;
    --text-light: #f1f1f4;
  }
  html, body { margin: 0; padding: 0; }
  body { width: 848px; height: 1200px; overflow: hidden; position: relative; background: var(--cream); font-family: "Carlito", "Calibri", sans-serif; }
  .backdrop-top { position: absolute; left: 0; top: 0; width: 550px; height: 545px; background: linear-gradient(135deg, var(--teal) 0%, #b9ddd2 45%, var(--teal) 100%); }
  .backdrop-bottom { position: absolute; left: 0; top: 545px; width: 550px; height: 655px; background: linear-gradient(160deg, #3a3a3a 0%, #8d8a85 50%, #2a2a2a 100%); }
  .divider { position: absolute; left: 532px; top: 0; width: 18px; height: 1200px; background: var(--paper); border-left: 2px solid #9a9a9a; border-right: 2px solid #9a9a9a; box-sizing: border-box; }
  .sidebar { position: absolute; left: 550px; top: 0; width: 298px; height: 1200px; background: linear-gradient(180deg, var(--slate-dark) 0, var(--slate) 55px, var(--slate) 1150px, var(--slate-dark) 1200px); color: var(--text-light); }
  .sheet { position: absolute; left: 69px; top: 53px; width: 463px; height: 1095px; background: var(--paper); }
  .photo { position: absolute; left: 21px; width: 176px; background: linear-gradient(180deg, #5b5b5b 0%, #b9b9b9 40%, #d8d8d8 65%, #3e3e3e 100%); }
  .photo-one { top: 66px; height: 159px; }
  .photo-two { top: 519px; height: 157px; }
  .section { position: absolute; left: 214px; width: 232px; hyphens: auto; -webkit-hyphens: auto; }
  .section-one { top: 64px; }
  .section-two { top: 515px; }
  h2 { font-family: "Oswald", sans-serif; font-weight: 500; color: var(--purple); text-transform: uppercase; margin: 0; letter-spacing: -0.3px; }
  .sheet h2 { font-size: 29px; line-height: 30px; }
  .section p { margin: 0; font-size: 13.6px; line-height: 20px; color: var(--text); }
  .section-one h2 { margin-bottom: 17px; }
  .section-two h2 { margin-bottom: 36px; }
  .sidebar-block { position: absolute; left: 32px; width: 232px; hyphens: auto; -webkit-hyphens: auto; }
  .offer { top: 137px; }
  .experience { top: 456px; }
  .sidebar h2 { color: var(--lilac); font-size: 28px; line-height: 34px; margin-bottom: 23px; }
  .sidebar p { margin: 0; font-size: 13.4px; line-height: 20px; }
  .sidebar ul { margin: 0; padding: 0 0 0 17px; font-size: 13.4px; line-height: 20px; }
</style>
</head>
<body>
  <div class="backdrop-top" role="img" aria-label="Decoratief streeppatroon in mintgroen en crème"></div>
  <div class="backdrop-bottom" role="img" aria-label="Decoratief streeppatroon in zwart en wit"></div>

  <main class="sheet">
    <div class="photo photo-one" role="img" aria-label="Zwart-witfoto: persoon houdt een bord vast met de tekst 'De klantvraag staat centraal ALTIJD'"></div>
    <section class="section section-one">
      <h2>Maatschap<br>Veltrix</h2>
      <p>De maten vormen een collectief van initiatiefrijke, ervaren (15 jaar of meer) en gedreven zelfstandige ondernemers. We vinden dat de bedrijfsvraagstukken leidend zijn. IT-producten en -pakketten, architectuur, methoden en technieken zijn hulpmiddelen en geen doelen op zich.</p>
      <p>Het ondersteunen van de opdrachtgever bij het demand-vraagstuk en het stellen van de goede vraag aan de IT-leverende partij, staat bij ons centraal.</p>
      <p>We zijn zelfstandig ondernemers zonder binding aan een product of methode. We zijn een verrijking, geen beperking van uw organisatie en we voeren uw agenda uit.</p>
    </section>

    <div class="photo photo-two" role="img" aria-label="Zwart-witfoto: persoon houdt een bord vast met de tekst 'Belangrijke beslissingen aanpakken met architectuur'"></div>
    <section class="section section-two">
      <h2>Hoe we werken</h2>
      <p>We helpen de beslisser beslissen. Dit doen we door de business eisen en wensen helder te maken en die te vertalen in (business en IT) oplossingen. Het vormen van oplossingen doen we door het toepassen van, door de jaren heen, bij andere klanten opgebouwde best practices.</p>
      <p>Elk van onze ondernemers wordt ondersteund door een omvangrijk kennisnetwerk. We wisselen ervaringen uit en bouwen actief aan onze vakkennis. Op die manier garanderen we dat onze kennis up-to-date is en relevant blijft.</p>
      <p>De maatschap levert een onder de door de Fiscale Rijksdienst goedgekeurde</p>
    </section>
  </main>

  <div class="divider"></div>

  <aside class="sidebar">
    <section class="sidebar-block offer">
      <h2>Wat we bieden</h2>
      <p>Een greep uit de bedrijfs- en IT-vraagstukken waarbij we helpen:</p>
      <ul>
        <li>IT strategie;</li>
        <li>Procesinrichting en -harmonisatie;</li>
        <li>Portfolio management;</li>
        <li>Inrichten van governance;</li>
        <li>Business - IT alignment,<br>IT transformatie;</li>
        <li>Innovatie en vernieuwing;</li>
        <li>Scenario analyse.</li>
      </ul>
      <p>Daarnaast bieden we architectuurtraining, -opleiding en -coaching.</p>
    </section>
    <section class="sidebar-block experience">
      <h2>Ervaring</h2>
      <p>De maten hebben werkervaring in overheid, zorg, onderwijs, transport, telecom, media, financiële dienstverlening, verzekeringen en nutsbedrijven. De maten zijn gecertificeerd voor gangbare methoden en industrie standaarden:</p>
      <ul>
        <li>BPM en Lean Flow Methode;</li>
        <li>IAK, DVA, OPAF en GAE;</li>
        <li>Modelvorm;</li>
        <li>SPRINT en FLOW;</li>
        <li>BIBL/ABL/ITBL;</li>
        <li>IREQ.</li>
      </ul>
    </section>
  </aside>
</body>
</html>
```